" Atua no ramo de diagnostico por imagem veterinário realizando exames de raio x, ultrassonografia, tomografia computadorizada e ressonância magnética para animais de companhia. "

```html
<!DOCTYPE html>
<html lang="pt-BR">
<head>
<meta charset="UTF-8">
<title>VETRA – Envelope Saco</title>
<link href="https://fonts.googleapis.com/css2?family=Montserrat:wght@400;500;600&display=swap" rel="stylesheet">
<style>
  :root {
    --backdrop: #a9a9a9;
    --navy: #174a6e;
    --green: #1f9a45;
    --paper: #ffffff;
    --label: #2b2b2b;
    --contact: #dce6ee;
  }
  * { margin: 0; padding: 0; box-sizing: border-box; }
  html, body { width: 1200px; height: 1200px; overflow: hidden; }
  body {
    background: var(--backdrop);
    font-family: "Montserrat", Arial, sans-serif;
    position: relative;
  }
  .sheet-label {
    position: absolute; left: 26px; top: 70px;
    font-size: 22px; color: var(--label); letter-spacing: 0.5px;
  }
  .envelope {
    position: absolute; left: 149px; top: 247px;
    width: 907px; height: 641px;
  }
  .envelope-back {
    position: absolute; left: 0; top: 0; width: 415px; height: 641px;
    background: var(--navy);
  }
  .envelope-front {
    position: absolute; left: 415px; top: 0; width: 492px; height: 641px;
    background: var(--paper);
  }
  .envelope svg.trim { position: absolute; left: 0; top: 0; }
  .brand {
    position: absolute; display: flex; align-items: center;
    font-weight: 500; letter-spacing: 2px;
  }
  .brand-dot { border-radius: 50%; flex: none; }
  .brand-front { left: 140px; top: 280px; }
  .brand-front .brand-dot { width: 58px; height: 58px; border: 5px solid var(--green); margin-right: 14px; }
  .brand-front .brand-name { font-size: 58px; color: var(--navy); line-height: 1; }
  .brand-tagline {
    position: absolute; left: 212px; top: 346px;
    font-size: 8.5px; font-weight: 600; color: var(--green); letter-spacing: 0.3px;
    text-transform: uppercase;
  }
  .brand-back { left: 130px; top: 518px; }
  .brand-back .brand-dot { width: 36px; height: 36px; border: 4px solid var(--paper); margin-right: 10px; }
  .brand-back .brand-name { font-size: 38px; color: var(--paper); line-height: 1; }
  .contact {
    position: absolute; top: 578px; font-size: 9.5px; color: var(--contact); line-height: 14px;
  }
  .contact li { list-style: none; display: flex; gap: 6px; }
  .contact li::before { content: ""; width: 5px; height: 5px; margin-top: 4px; border-radius: 50%; background: var(--green); flex: none; }
  .contact-left { left: 80px; }
  .contact-right { left: 235px; }
</style>
</head>
<body>
  <div class="sheet-label">ENVELOPE SACO</div>

  <div class="envelope">
    <div class="envelope-back">
      <div class="brand brand-back"><span class="brand-dot"></span><span class="brand-name">VETRA</span></div>
      <ul class="contact contact-left">
        <li>(00) 0000.0000 / 00000.0000</li>
        <li>contato@vetradiag.com.br</li>
      </ul>
      <ul class="contact contact-right">
        <li>www.vetradiag.com.br</li>
        <li>End. completo, 00, Bairro<br>CEP 0000-000 - Cidade-SP</li>
      </ul>
    </div>
    <div class="envelope-front">
      <div class="brand brand-front"><span class="brand-dot"></span><span class="brand-name">VETRA</span></div>
      <div class="brand-tagline">Centro de diagnóstico por imagem veterinário</div>
    </div>
    <svg class="trim" width="907" height="641" viewBox="0 0 907 641">
      <polygon points="8,0 408,0 392,70 24,70" fill="var(--green)"/>
      <rect x="0" y="632" width="415" height="9" fill="var(--green)"/>
      <polygon points="820,632 907,618 907,641 810,641" fill="var(--green)"/>
    </svg>
  </div>
</body>
</html>
```